Design a chocolate bar wrapper

We want to make a chocolate bar with the name "quiet meadow". We hope to make a mushroom bar with healing benefits. Looking to pick 2-3 winners to flush out the design

The name quiet meadow is used to describe a mushroom cap when looking at the top part of it.

```html
<!DOCTYPE html>
<html lang="en">
<head>
<meta charset="UTF-8">
<title>Quiet Meadow – Chocolate Bar Wrapper</title>
<link rel="stylesheet" href="https://fonts.googleapis.com/css2?family=Cinzel:wght@500&display=swap">
<style>
  :root {
    --backdrop: #cbb6b5;
    --wrapper: #5b2b26;
    --wrapper-deep: #4a211d;
    --crimp: #42201c;
    --crimp-line: #371a17;
    --ink-light: #f4ece8;
    --glow: #e0662e;
    --cap: #b58a6e;
  }
  * { box-sizing: border-box; margin: 0; padding: 0; }
  html, body {
    width: 1200px;
    height: 1200px;
    overflow: hidden;
    background: var(--backdrop);
  }
  .canvas {
    position: relative;
    width: 1200px;
    height: 1200px;
    display: flex;
    align-items: center;
    justify-content: center;
  }
  .wrapper {
    position: relative;
    width: 440px;
    height: 1020px;
    background: radial-gradient(ellipse at 50% 45%, var(--wrapper) 0%, var(--wrapper-deep) 100%);
    box-shadow: inset 0 0 40px rgba(0,0,0,0.25);
  }
  .crimp {
    position: absolute;
    left: 0;
    width: 100%;
    height: 64px;
    background: repeating-linear-gradient(90deg, var(--crimp) 0 6px, var(--crimp-line) 6px 8px);
  }
  .crimp--top { top: 0; border-bottom: 2px solid var(--crimp-line); }
  .crimp--bottom { bottom: 0; border-top: 2px solid var(--crimp-line); }
  .brand-name {
    position: absolute;
    top: 300px;
    left: 50%;
    width: 520px;
    transform: translate(-50%, -50%) rotate(90deg);
    font-family: "Cinzel", serif;
    font-weight: 500;
    font-size: 86px;
    line-height: 1.05;
    letter-spacing: 4px;
    color: var(--ink-light);
    text-align: center;
  }
  .brand-name span { display: block; }
  .mushroom-art {
    position: absolute;
    left: 60px;
    top: 560px;
    width: 340px;
    height: 380px;
    border-radius: 40% 45% 35% 40%;
    background:
      radial-gradient(circle at 55% 55%, var(--glow) 0%, rgba(224,102,46,0.55) 25%, transparent 55%),
      radial-gradient(ellipse at 40% 40%, var(--cap) 0%, rgba(181,138,110,0.4) 45%, transparent 75%);
  }
</style>
</head>
<body>
  <main class="canvas">
    <section class="wrapper" aria-label="Quiet Meadow chocolate bar wrapper">
      <div class="crimp crimp--top"></div>
      <h1 class="brand-name"><span>Quiet</span><span>Meadow</span></h1>
      <div class="mushroom-art" role="img" aria-label="Illustration of mushroom caps and stems tumbling together with a warm orange glow between them"></div>
      <div class="crimp crimp--bottom"></div>
    </section>
  </main>
</body>
</html>
```